Business card for home decor store and design

I need a business card for my home decor boutique that’s professional looking boho/rustic. We sell vintage furniture, vintage finds, lamps, throws, rugs. We also carry a Diy paint line for refinishing furniture. We offer workshop on painting furniture, private or group setting. We in the heart of Old Town Red Bluff. We love to design, build and restore. Family owned small business. Our style is rustic boho farmhouse. We search for one of a kind found and repurposed items. We love vintage home decor, vintage windows.

Target Market(s)

Home decor

Industry/Entity Type

Home Accessories

Contact Information for Business Card

Have a rustic look/boho

Font styles to use
Serif
Script

Requirements
Must have
• Logo

```html
<!DOCTYPE html>
<html lang="en">
<head>
<meta charset="utf-8">
<title>Hearth &amp; Ember Co. — Business Card</title>
<link rel="stylesheet" href="https://fonts.googleapis.com/css2?family=Montserrat:wght@400;600&display=swap">
<style>
  :root {
    --backdrop: #1c1c1d;
    --card-white: #ffffff;
    --ink: #161616;
    --ink-soft: #3a3a3a;
    --clay: #5a3f2e;
    --clay-light: #6b4c39;
    --clay-deep: #47301f;
  }
  * { box-sizing: border-box; margin: 0; padding: 0; }
  html, body {
    width: 1200px; height: 711px; overflow: hidden;
    background: var(--backdrop);
    font-family: "Montserrat", sans-serif;
  }
  .canvas {
    width: 1200px; height: 711px;
    display: flex; align-items: center; justify-content: center; gap: 60px;
  }
  .card {
    width: 520px; height: 298px; position: relative;
    border-radius: 3px; overflow: hidden;
  }
  .card--front { background: var(--card-white); color: var(--ink); }
  .card--back  {
    background: linear-gradient(160deg, var(--clay-light), var(--clay) 55%, var(--clay-deep));
  }

  .brand {
    position: absolute; display: flex; align-items: center; gap: 10px;
    font-weight: 600; letter-spacing: 0.02em; white-space: nowrap;
  }
  .brand__dot {
    border-radius: 50%; border: 2px solid currentColor; flex: none;
  }
  .card--front .brand { top: 34px; right: 36px; font-size: 20px; color: var(--ink); }
  .card--front .brand__dot { width: 22px; height: 22px; }

  .rule { position: absolute; height: 1.5px; background: var(--ink); }
  .rule--top { top: 88px; left: 36px; right: 36px; }
  .rule--bottom { top: 220px; left: 36px; width: 190px; }

  .web-info {
    position: absolute; top: 104px; right: 36px;
    list-style: none; text-align: right; font-size: 11px; color: var(--ink-soft);
    line-height: 1.8; letter-spacing: 0.03em;
  }
  .person { position: absolute; left: 36px; top: 168px; }
  .person__name { font-size: 18px; font-weight: 600; letter-spacing: 0.06em; }
  .person__title { font-size: 11px; font-weight: 400; letter-spacing: 0.14em; color: var(--ink-soft); margin-top: 4px; }

  .contact {
    position: absolute; left: 36px; top: 232px; list-style: none;
    font-size: 11px; color: var(--ink-soft); line-height: 1.9; letter-spacing: 0.03em;
  }
  .contact li, .web-info li { display: flex; align-items: center; gap: 7px; }
  .web-info li { justify-content: flex-end; }
  .icon { width: 10px; height: 10px; fill: var(--ink); flex: none; }

  .card--back .brand {
    top: 50%; left: 50%; transform: translate(-50%, -50%);
    font-size: 30px; color: var(--clay-light);
    text-shadow: none;
  }
  .card--back .brand__dot { width: 30px; height: 30px; border-color: var(--clay-light); }
</style>
</head>
<body>
<main class="canvas">
  <section class="card card--front" aria-label="Card front">
    <div class="brand"><span class="brand__dot"></span>Hearth &amp; Ember Co.</div>
    <div class="rule rule--top"></div>
    <ul class="web-info">
      <li>www.weburl.xyz
        <svg class="icon" viewBox="0 0 10 10"><circle cx="5" cy="5" r="4.3" fill="none" stroke="#161616" stroke-width="1.1"/><ellipse cx="5" cy="5" rx="1.8" ry="4.3" fill="none" stroke="#161616" stroke-width="0.9"/><line x1="0.7" y1="5" x2="9.3" y2="5" stroke="#161616" stroke-width="0.9"/></svg>
      </li>
      <li>address here
        <svg class="icon" viewBox="0 0 10 10"><path d="M5 0.5a3.3 3.3 0 0 0-3.3 3.3C1.7 6.3 5 9.5 5 9.5s3.3-3.2 3.3-5.7A3.3 3.3 0 0 0 5 0.5zm0 4.6a1.3 1.3 0 1 1 0-2.6 1.3 1.3 0 0 1 0 2.6z"/></svg>
      </li>
    </ul>
    <div class="person">
      <h1 class="person__name">YOUR NAME</h1>
      <p class="person__title">JOB TITLE</p>
    </div>
    <div class="rule rule--bottom"></div>
    <ul class="contact">
      <li>
        <svg class="icon" viewBox="0 0 10 10"><path d="M2.2 0.6l1.6 1.9-0.9 1.2c0.6 1.3 1.6 2.3 2.9 2.9l1.2-0.9 1.9 1.6-0.9 1.5C4.6 8.8 1.2 5.4 0.7 1.5z"/></svg>
        000 000 0000
      </li>
      <li>
        <svg class="icon" viewBox="0 0 10 10"><path d="M0.5 2h9v6h-9z M0.5 2l4.5 3.5 4.5-3.5" fill="#161616" stroke="#fff" stroke-width="0.7"/></svg>
        youremail@xyz.com
      </li>
    </ul>
  </section>

  <section class="card card--back" aria-label="Card back">
    <div class="brand"><span class="brand__dot"></span>Hearth &amp; Ember Co.</div>
  </section>
</main>
</body>
</html>
```